Mr Polish Stationery Design Project
Business card, letterhead, with compliments slip design
Use standard fonts
that suit the logo design
Professional
Neil Hartley
Director
Head Office: PO Box 814,
Kirrawee NSW 2232
1300 MRPOLISH (number as well)
neil@mrpolish-demo.com.au
www.mrpolish-demo.com.au
Licensed Repairer MVRL84017
1. all stationery needs to carry the following:
'The Perfect Finish' as a slogan.
2. A4 letterhead to include a watermark (either logo or sillouette of prestige car)
3. DL with compliments slip to be also designed
Mr Polish Services:
- Hail Damage
- Dent Removal
- Commercial and Retail
- Insurance
- Vandalism Damage
the address can be placed on the reverse of the card if front is to crowded.
For more information regarding the company see brief from logo project previously run on markmakerhub. 95% of work performed by the company is in the automotive industry
The logo design has been created so that it works on both a black background and white background. The company is happy to see the logo be used on both colours. ie. letterhead white background and business card on black background as long as the design is consistent with both.
here is the version for black backgrounds. Unfortunately at this moment I only have a jpg of this file. the correct ai logo will be upload as soosn as possible.

```html
<!DOCTYPE html>
<html lang="en">
<head>
<meta charset="utf-8">
<title>Mr Polish Stationery</title>
<link href="https://fonts.googleapis.com/css2?family=Exo+2:wght@800&family=Open+Sans:ital,wght@0,400;0,600;1,400&display=swap" rel="stylesheet">
<style>
  :root{
    --page:#ffffff;
    --paper:#ffffff;
    --edge:#d6d6d6;
    --ink:#3a3a3a;
    --muted:#7a7a7a;
    --green:#7bc043;
    --green-deep:#3f8f2a;
    --card:#0d0d0d;
    --card-ink:#e8e8e8;
    --card-muted:#bdbdbd;
  }
  *{box-sizing:border-box;margin:0;padding:0}
  html,body{width:1200px;height:427px;overflow:hidden;background:var(--page)}
  body{position:relative;font-family:"Open Sans",Arial,sans-serif;color:var(--ink)}

  .sheet{position:absolute;background:var(--paper);box-shadow:0 0 0 1px var(--edge),2px 3px 6px rgba(0,0,0,.18);overflow:hidden}
  .corner-band{position:absolute;top:0;right:0;background:linear-gradient(200deg,#6e6e6e 0%,#bdbdbd 35%,rgba(123,192,67,.55) 55%,rgba(255,255,255,0) 80%)}
  .side-band{position:absolute;top:0;bottom:0;background:linear-gradient(90deg,rgba(255,255,255,0),rgba(123,192,67,.35) 50%,rgba(255,255,255,0))}

  .brand{position:absolute;line-height:1}
  .brand-name{font-family:"Exo 2",Arial,sans-serif;font-weight:800;color:var(--ink);letter-spacing:.3px;display:flex;align-items:center;gap:4px;white-space:nowrap}
  .brand-dot{display:inline-block;border-radius:50%;background:var(--green);flex:none}
  .brand-tagline{color:var(--green-deep);font-weight:600;margin-top:2px;white-space:nowrap}
  .contact{position:absolute;color:var(--muted);line-height:1.35;white-space:nowrap}

  /* A4 letterhead */
  .letterhead{left:43px;top:12px;width:221px;height:401px}
  .letterhead .corner-band{width:90px;height:34px}
  .letterhead .brand{left:16px;top:16px}
  .letterhead .brand-name{font-size:14px}
  .letterhead .brand-dot{width:5px;height:5px}
  .letterhead .brand-tagline{font-size:5px}
  .letterhead .contact{left:16px;top:42px;font-size:4px}
  .watermark{position:absolute;left:30px;right:30px;top:170px;height:60px;border-radius:30px 40px 8px 8px;background:radial-gradient(ellipse at center,rgba(0,0,0,.05),rgba(0,0,0,0) 70%)}

  /* Envelope */
  .envelope{left:336px;top:91px;width:454px;height:264px}
  .envelope .flap{position:absolute;right:0;top:0;width:30px;height:100%;border-left:1px solid var(--edge)}
  .envelope .side-band{right:22px;width:28px}
  .envelope .brand{left:19px;top:17px}
  .envelope .brand-name{font-size:15px}
  .envelope .brand-dot{width:5px;height:5px}
  .envelope .brand-tagline{font-size:5px}
  .envelope .contact{left:19px;top:45px;font-size:4px}

  /* Business cards */
  .card{left:931px;width:64px;height:82px;background:var(--card);box-shadow:1px 2px 5px rgba(0,0,0,.3)}
  .card-front{top:79px}
  .card-back{top:166px;height:74px}
  .card .corner-band{width:40px;height:14px;background:linear-gradient(200deg,rgba(123,192,67,.7),rgba(13,13,13,0) 75%)}
  .card .brand{left:6px;top:12px}
  .card .brand-name{font-size:8px;color:var(--card-ink)}
  .card .brand-dot{width:3px;height:3px}
  .card .brand-tagline{font-size:3px;color:var(--green)}
  .card .contact{left:6px;top:52px;font-size:3px;color:var(--card-muted)}
  .card-back .contact{left:0;right:0;top:12px;text-align:center}
  .card-back .person{color:var(--card-ink);font-weight:600}
  .car-silhouette{position:absolute;left:8px;right:8px;bottom:10px;height:16px;border-radius:8px 10px 2px 2px;background:linear-gradient(180deg,rgba(123,192,67,.3),rgba(123,192,67,.05))}

  /* With compliments slip */
  .slip{left:828px;top:247px;width:330px;height:161px}
  .slip .corner-band{width:140px;height:34px}
  .slip .brand{left:16px;top:26px}
  .slip .brand-name{font-size:16px}
  .slip .brand-dot{width:5px;height:5px}
  .slip .brand-tagline{font-size:5px}
  .slip .contact{left:16px;top:56px;font-size:4px}
  .compliments{position:absolute;right:14px;bottom:12px;font-style:italic;font-size:10px;color:var(--muted);white-space:nowrap}
</style>
</head>
<body>

<section class="sheet letterhead" aria-label="Letterhead">
  <div class="corner-band" role="img" aria-label="Grey and green sweep in the top corner"></div>
  <div class="brand">
    <div class="brand-name"><span class="brand-dot"></span>Mr Polish</div>
    <div class="brand-tagline">The Perfect Finish</div>
  </div>
  <div class="contact">Head Office: PO Box 814, Kirrawee NSW 2232<br>Ph: 1300 MRPOLISH · neil@mrpolish-demo.com.au<br>www.mrpolish-demo.com.au</div>
  <div class="watermark" role="img" aria-label="Faint watermark silhouette of a prestige car"></div>
</section>

<section class="sheet envelope" aria-label="Envelope">
  <div class="side-band" role="img" aria-label="Green sweep running down beside the flap"></div>
  <div class="flap"></div>
  <div class="brand">
    <div class="brand-name"><span class="brand-dot"></span>Mr Polish</div>
    <div class="brand-tagline">The Perfect Finish</div>
  </div>
  <div class="contact">Head Office: PO Box 814, Kirrawee NSW 2232<br>Ph: 1300 MRPOLISH · www.mrpolish-demo.com.au</div>
</section>

<section class="sheet card card-front" aria-label="Business card front">
  <div class="corner-band" role="img" aria-label="Green sweep in the top corner"></div>
  <div class="brand">
    <div class="brand-name"><span class="brand-dot"></span>Mr Polish</div>
    <div class="brand-tagline">The Perfect Finish</div>
  </div>
  <div class="contact">Licensed Repairer<br>MVRL84017</div>
</section>

<section class="sheet card card-back" aria-label="Business card back">
  <div class="contact"><span class="person">Neil Hartley</span><br>Director<br>1300 MRPOLISH<br>neil@mrpolish-demo.com.au</div>
  <div class="car-silhouette" role="img" aria-label="Green outline silhouette of a prestige car"></div>
</section>

<section class="sheet slip" aria-label="With compliments slip">
  <div class="corner-band" role="img" aria-label="Grey and green sweep in the top corner"></div>
  <div class="brand">
    <div class="brand-name"><span class="brand-dot"></span>Mr Polish</div>
    <div class="brand-tagline">The Perfect Finish</div>
  </div>
  <div class="contact">Head Office: PO Box 814, Kirrawee NSW 2232<br>Ph: 1300 MRPOLISH · neil@mrpolish-demo.com.au</div>
  <div class="compliments">With Compliments</div>
</section>

</body>
</html>
```